ZUMRA Virtualizing the computer, making it live in the cloud

We plan to visualize the computer, essentially making all your computing, storage, security, processing, etc done in the cloud. We feel this will revolutionize the entire computer industry.
We have a logo design which has been included here. We want this sharp, progressive and also frameworked in a way that we can sell our monthly service as well as computers online through this site.

Target Market(s)

Laptop users, Millennials, college educated people.

Industry/Entity Type

Computer

Number of Pages Required

5+ page

Font styles to use
Serif
Sans Serif

Colors

Designer to choose colors to be used in the design.

Requirements
Must have
• eCommerce capable. Frameworked for people to enroll in our program and pay for the service online. Would prefer to allow people from multiple countries to enroll and use our service

```html
<!DOCTYPE html>
<html lang="en">
<head>
<meta charset="utf-8">
<title>ZUMRA — Cloud Computing</title>
<link rel="stylesheet" href="https://fonts.googleapis.com/css2?family=Quicksand:wght@500;700&family=Open+Sans:wght@400;600;700&family=Roboto:wght@400;500&display=swap">
<style>
:root{
  --ink:#2f2f2f;
  --muted:#555;
  --gold:#dbb600;
  --gold-btn:#d9b90a;
  --olive:#b5aa0e;
  --olive-deep:#9c9108;
  --white:#fff;
  --grey-band:#efefef;
  --footer:#323331;
  --field:#ececec;
}
*{box-sizing:border-box;margin:0;padding:0}
html,body{width:1200px;height:3109px;overflow:hidden}
body{position:relative;font-family:"Open Sans",Arial,sans-serif;color:var(--ink);background:var(--white)}
.abs{position:absolute}

/* Hero */
.hero{left:0;top:0;width:1200px;height:684px;background:linear-gradient(90deg,#080a08 0%,#0f160e 45%,#1d3418 70%,#2a4d22 100%)}
.hero-visual{left:500px;top:0;width:700px;height:684px;background:radial-gradient(circle at 62% 48%,rgba(140,220,100,.45) 0%,rgba(70,140,50,.3) 30%,rgba(20,40,18,0) 70%)}
.brand{left:100px;top:34px;font-family:"Quicksand",sans-serif;font-weight:700;font-size:44px;color:var(--white);display:flex;align-items:center;gap:10px;letter-spacing:1px}
.brand-dot{width:14px;height:14px;border-radius:50%;background:var(--gold)}
.top-contact{right:98px;top:22px;display:flex;gap:28px;color:var(--white);font-size:17px;font-family:"Roboto",sans-serif}
.top-contact span{display:flex;align-items:center;gap:10px}
.nav{right:98px;top:78px;display:flex;gap:40px;font-family:"Roboto",sans-serif;font-weight:500;font-size:15px;color:var(--white);letter-spacing:.3px}
.hero-title{left:100px;top:228px;font-family:"Quicksand",sans-serif;font-weight:700;font-size:42px;color:var(--white);letter-spacing:.5px}
.hero-text{left:100px;top:302px;width:520px;font-size:15px;line-height:31px;color:var(--white);font-weight:600}
.btn-outline-light{left:100px;top:398px;width:108px;height:46px;border:2px solid var(--white);color:var(--white);font-size:14px;font-weight:600;display:flex;align-items:center;justify-content:center}
.hero-arrows{left:98px;top:498px;display:flex;gap:8px}

/* About */
.section-title{font-family:"Quicksand",sans-serif;font-weight:700;font-size:27px;color:var(--gold)}
.about-title{left:100px;top:742px}
.about-text{left:100px;top:812px;width:612px;font-size:13.5px;line-height:23px;color:var(--muted)}
.about-text p+p{margin-top:12px}
.btn-gold{background:var(--gold-btn);color:var(--white);font-size:14px;font-weight:600;display:flex;align-items:center;justify-content:center}
.about-read{left:100px;top:986px;width:108px;height:42px}
.btn-outline-dark{border:1.5px solid #444;color:var(--ink);font-size:14px;font-weight:600;display:flex;align-items:center;justify-content:center}
.about-contact{left:220px;top:986px;width:108px;height:42px}
.about-visual{left:763px;top:770px;width:326px;height:246px;background:radial-gradient(circle at 50% 55%,#cfe8f8 0%,#e9f4fb 55%,#fff 80%);border-radius:8px}

/* Services */
.services{left:0;top:1088px;width:1200px;height:616px;background:linear-gradient(120deg,var(--olive-deep) 0%,var(--olive) 45%,#c2b612 100%);clip-path:polygon(0 0,100% 44px,100% 100%,0 95%)}
.services-title{left:0;width:1200px;top:1178px;text-align:center;color:var(--white);font-family:"Quicksand",sans-serif;font-weight:700;font-size:27px}
.services-rule{left:535px;top:1230px;width:130px;height:2px;background:var(--white)}
.service{top:1292px;width:250px;text-align:center;color:var(--white)}
.service-icon{margin:0 auto;display:block}
.service h3{font-family:"Roboto",sans-serif;font-weight:500;font-size:20px;margin-top:22px}
.service p{font-size:13px;line-height:22px;margin:12px auto 0;width:200px}
.service-divider{top:1320px;width:1px;height:290px;background:rgba(255,255,255,.35)}
.slide-arrow{top:1415px}

/* Process */
.process-visual{left:97px;top:1828px;width:302px;height:224px;background:linear-gradient(160deg,#3b3b3b 0%,#2a7fd1 45%,#58b4f0 70%,#dfe7ee 100%);border-radius:6px}
.process-title{left:539px;top:1762px}
.process-rule{left:539px;top:1812px;width:285px;height:1.5px;background:var(--gold)}
.step{left:540px;width:560px;display:flex;gap:24px}
.step h4{font-family:"Roboto",sans-serif;font-weight:500;font-size:16.5px;color:var(--ink)}
.step p{font-size:13.5px;line-height:26px;color:var(--muted);margin-top:10px}

/* Blog */
.blog{left:0;top:2166px;width:1200px;height:456px;background:var(--grey-band);clip-path:polygon(0 0,100% 36px,100% 100%,0 88%)}
.blog-title{left:0;width:1200px;top:2244px;text-align:center}
.post{top:2355px;display:flex;gap:18px;width:500px}
.post-img{width:196px;height:158px;flex:none}
.post h4{font-family:"Roboto",sans-serif;font-weight:500;font-size:16.5px;color:var(--ink);margin-top:6px}
.post .by{font-size:11.5px;font-style:italic;color:var(--gold);margin-top:6px}
.post p{font-size:12.5px;line-height:23px;color:var(--muted);margin-top:8px}

/* Footer */
.footer{left:0;top:2622px;width:1200px;height:487px;background:var(--footer)}
.footer-heading{color:var(--white);font-family:"Roboto",sans-serif;font-weight:500;font-size:20px}
.form-heading{color:var(--white);font-family:"Open Sans",sans-serif;font-weight:600;font-size:17px}
.contact-list{left:100px;top:2762px;color:var(--white)}
.contact-item{display:flex;align-items:center;gap:22px;font-size:15px;font-weight:600;line-height:26px}
.contact-item+.contact-item{margin-top:26px}
.contact-ring{width:50px;height:50px;border:1.5px solid rgba(255,255,255,.8);border-radius:50%;display:flex;align-items:center;justify-content:center;flex:none}
.form-field{background:var(--field);color:#8a8a8a;font-size:13px;padding:11px 12px;height:42px}
.form-send{left:485px;top:2952px;width:116px;height:35px;font-size:13px}
.footer-rule{left:100px;top:3022px;width:1000px;height:1px;background:rgba(255,255,255,.3)}
.copyright{left:100px;top:3056px;font-size:13px;color:var(--white)}
.social{top:3044px;width:38px;height:38px;border:1.5px solid var(--white);border-radius:50%}
</style>
</head>
<body>

<!-- Hero -->
<section class="abs hero"></section>
<div class="abs hero-visual" role="img" aria-label="Photo of a hand reaching toward a glowing cloud network with service icons"></div>
<div class="abs brand"><span class="brand-dot"></span>zumra</div>
<div class="abs top-contact">
  <span><svg width="26" height="26" viewBox="0 0 26 26"><circle cx="13" cy="13" r="12" fill="none" stroke="#fff" stroke-width="1.6"/><path d="M9 8l3 0 1 3-2 1.5a7 7 0 0 0 3.5 3.5L16 14l3 1v3a1 1 0 0 1-1 1A10 10 0 0 1 8 9a1 1 0 0 1 1-1z" fill="#fff"/></svg>180 555 0147</span>
  <span><svg width="26" height="26" viewBox="0 0 26 26"><circle cx="13" cy="13" r="12" fill="none" stroke="#fff" stroke-width="1.6"/><rect x="7.5" y="9" width="11" height="8" fill="none" stroke="#fff" stroke-width="1.4"/><path d="M7.5 9l5.5 4.5L18.5 9" fill="none" stroke="#fff" stroke-width="1.4"/></svg>hello@zumra-cloud.com</span>
</div>
<nav class="abs nav"><span>HOME</span><span>ABOUT US</span><span>BLOG</span><span>OUR SERVICES</span><span>CONTACT US</span></nav>
<h1 class="abs hero-title">WELCOME TO ZUMRA</h1>
<p class="abs hero-text">We make all your computing, storage, security, processing, etc done in the cloud.</p>
<div class="abs btn-outline-light">Read More</div>
<div class="abs hero-arrows">
  <svg width="26" height="26" viewBox="0 0 26 26"><circle cx="13" cy="13" r="13" fill="#fff"/><path d="M15 7l-6 6 6 6M9 13h10" stroke="#111" stroke-width="2.4" fill="none"/></svg>
  <svg width="26" height="26" viewBox="0 0 26 26"><circle cx="13" cy="13" r="13" fill="#fff"/><path d="M11 7l6 6-6 6M7 13h10" stroke="#111" stroke-width="2.4" fill="none"/></svg>
</div>

<!-- About -->
<h2 class="abs section-title about-title">About zumra</h2>
<div class="abs about-text">
  <p>Nemo enim ipsam voluptatem quia voluptas sit aspernatur aut odit aut fugit, sed quia conse quuntur magni dolores eos qui ratione voluptatem sequi nesciunt. Neque porro quisquam est, qui dolorem ipsum quia dolor sit amet, consectetur.</p>
  <p>Sed ut perspiciatis unde omnis iste natus error sit voluptatem accusantium doloremque laudan tium, totam rem aperiam, eaque ipsa quae ab illo inventore veritatis et quasi architecto beatae vitae dicta sunt explicabo.</p>
</div>
<div class="abs btn-gold about-read">Read More</div>
<div class="abs btn-outline-dark about-contact">Contact Us</div>
<div class="abs about-visual" role="img" aria-label="Illustration of a blue cloud connected to a laptop, monitor, tower and phone"></div>

<!-- Services -->
<section class="abs services" role="img" aria-label="Olive-tinted photo of hands on a keyboard with network lines"></section>
<h2 class="abs services-title">Our zumra Services</h2>
<div class="abs services-rule"></div>
<svg class="abs slide-arrow" style="left:30px" width="30" height="56" viewBox="0 0 30 56"><path d="M28 2L3 28l25 26" fill="none" stroke="#fff" stroke-width="2"/></svg>
<svg class="abs slide-arrow" style="left:1140px" width="30" height="56" viewBox="0 0 30 56"><path d="M2 2l25 26L2 54" fill="none" stroke="#fff" stroke-width="2"/></svg>

<div class="abs service" style="left:107px">
  <svg class="service-icon" width="150" height="170" viewBox="0 0 150 170"><path d="M75 6a69 69 0 0 1 18 135.6L75 166l-18-24.4A69 69 0 0 1 75 6z" fill="none" stroke="#fff" stroke-width="3"/><circle cx="75" cy="75" r="56" fill="#fff"/><g fill="var(--olive)"><circle cx="75" cy="60" r="9"/><path d="M61 92a14 14 0 0 1 28 0z"/><circle cx="54" cy="66" r="7"/><path d="M42 92a12 12 0 0 1 20-9v9z"/><circle cx="96" cy="66" r="7"/><path d="M108 92a12 12 0 0 0-20-9v9z"/></g></svg>
  <h3>Computing</h3>
  <p>Nemo enim ipsam voluptatem quia voluptas sit aspernatur aut odit aut fugit.</p>
</div>
<div class="abs service-divider" style="left:398px"></div>
<div class="abs service" style="left:474px">
  <svg class="service-icon" width="150" height="170" viewBox="0 0 150 170"><path d="M75 6a69 69 0 0 1 18 135.6L75 166l-18-24.4A69 69 0 0 1 75 6z" fill="none" stroke="#fff" stroke-width="3"/><circle cx="75" cy="75" r="56" fill="#fff"/><g fill="var(--olive)"><circle cx="62" cy="66" r="12"/><circle cx="80" cy="60" r="15"/><circle cx="94" cy="70" r="10"/><rect x="52" y="66" width="52" height="14" rx="7"/></g><g stroke="var(--olive)" stroke-width="3" fill="none"><path d="M75 80v20M62 80v12h-8M88 80v12h8"/></g><g fill="var(--olive)"><circle cx="75" cy="103" r="4"/><circle cx="51" cy="92" r="4"/><circle cx="99" cy="92" r="4"/></g></svg>
  <h3>Storage</h3>
  <p>Nemo enim ipsam voluptatem quia voluptas sit aspernatur aut odit aut fugit.</p>
</div>
<div class="abs service-divider" style="left:773px"></div>
<div class="abs service" style="left:810px">
  <svg class="service-icon" width="150" height="170" viewBox="0 0 150 170"><path d="M75 6a69 69 0 0 1 18 135.6L75 166l-18-24.4A69 69 0 0 1 75 6z" fill="none" stroke="#fff" stroke-width="3"/><circle cx="75" cy="75" r="56" fill="#fff"/><rect x="46" y="50" width="58" height="40" fill="none" stroke="var(--olive)" stroke-width="4"/><path d="M53 82l14-14 10 8 19-19" fill="none" stroke="var(--olive)" stroke-width="4"/><path d="M90 56h7v7" fill="none" stroke="var(--olive)" stroke-width="3"/><path d="M64 100h22M75 90v10" stroke="var(--olive)" stroke-width="4"/></svg>
  <h3>Security</h3>
  <p>Nemo enim ipsam voluptatem quia voluptas sit aspernatur aut odit aut fugit.</p>
</div>

<!-- Process -->
<div class="abs process-visual" role="img" aria-label="Illustration of a monitor, tablet, phones and laptop each showing a cloud on a blue screen"></div>
<h2 class="abs section-title process-title">Process Done In The Cloud</h2>
<div class="abs process-rule"></div>
<div class="abs step" style="top:1840px">
  <svg width="44" height="44" viewBox="0 0 44 44" style="flex:none;margin-top:2px"><rect x="6" y="6" width="20" height="26" fill="none" stroke="var(--gold)" stroke-width="2.4"/><rect x="14" y="14" width="24" height="24" fill="none" stroke="var(--gold)" stroke-width="2.4"/><path d="M18 22h16M18 28h16M18 34h10" stroke="var(--gold)" stroke-width="2"/></svg>
  <div><h4>Cloud Computing</h4><p>Nemo enim ipsam voluptatem quia voluptas sit aspernatur aut odit aut fugit, sed quia consequuntur magni dolores eos qui ratione voluptatem.</p></div>
</div>
<div class="abs step" style="top:1943px">
  <svg width="44" height="44" viewBox="0 0 44 44" style="flex:none;margin-top:2px"><rect x="4" y="6" width="36" height="24" fill="none" stroke="var(--gold)" stroke-width="2.6"/><path d="M15 38h14M22 30v8" stroke="var(--gold)" stroke-width="3"/></svg>
  <div><h4>Storage And Security Processes</h4><p>Nemo enim ipsam voluptatem quia voluptas sit aspernatur aut odit aut fugit, sed quia consequuntur magni dolores eos qui ratione voluptatem.</p></div>
</div>
<div class="abs step" style="top:2046px">
  <svg width="44" height="44" viewBox="0 0 44 44" style="flex:none;margin-top:2px"><circle cx="14" cy="17" r="7" fill="var(--gold)"/><path d="M2 40a12 12 0 0 1 24 0z" fill="var(--gold)"/><rect x="24" y="4" width="18" height="13" rx="2" fill="none" stroke="var(--gold)" stroke-width="2"/><path d="M27 17l-2 5 6-5" fill="var(--gold)"/></svg>
  <div><h4>Virtualise Home Computer</h4><p>Nemo enim ipsam voluptatem quia voluptas sit aspernatur aut odit aut fugit, sed quia consequuntur magni dolores eos qui ratione voluptatem.</p></div>
</div>

<!-- Blog -->
<section class="abs blog"></section>
<h2 class="abs section-title blog-title">Our Blog Posts</h2>
<article class="abs post" style="left:100px">
  <div class="post-img" role="img" aria-label="Photo of a hand holding a tablet with glowing cloud icons" style="background:linear-gradient(135deg,#1f5f9a 0%,#5aa6e0 50%,#d7e8f4 100%)"></div>
  <div><h4>Nemo enim ipsam voluptatem</h4><div class="by">Posted by: corin</div><p>Sed ut perspiciatis unde omnis iste natus error sit voluptatem accusantium doloremque laudan tium totam rem aperiam, eaque ipsa quae illo inventore veritatis et quasi architector.</p></div>
</article>
<article class="abs post" style="left:616px">
  <div class="post-img" role="img" aria-label="Photo of a paper cloud held above a laptop on a desk" style="background:linear-gradient(160deg,#cbbfb0 0%,#8fb9d6 45%,#6b6b6b 100%)"></div>
  <div><h4>Neque porro quisquam</h4><div class="by">Posted by: corin</div><p>Sed ut perspiciatis unde omnis iste natus error sit voluptatem accusantium doloremque laudan tium totam rem aperiam, eaque ipsa quae illo inventore veritatis et quasi architector.</p></div>
</article>

<!-- Footer -->
<footer class="abs footer"></footer>
<h3 class="abs footer-heading" style="left:100px;top:2686px">Contact Us</h3>
<div class="abs contact-list">
  <div class="contact-item"><span class="contact-ring"><svg width="22" height="22" viewBox="0 0 22 22"><circle cx="11" cy="11" r="11" fill="#fff"/><rect x="5.5" y="7" width="11" height="8" fill="var(--footer)"/><path d="M5.5 7l5.5 4.5L16.5 7" stroke="#fff" stroke-width="1.2" fill="none"/></svg></span>hello@zumra-cloud.com</div>
  <div class="contact-item"><span class="contact-ring"><svg width="36" height="36" viewBox="0 0 36 36"><circle cx="18" cy="18" r="17" fill="#fff"/><path d="M18 8a7 7 0 0 1 7 7c0 5-7 13-7 13s-7-8-7-13a7 7 0 0 1 7-7z" fill="none" stroke="var(--gold)" stroke-width="2"/><circle cx="18" cy="15" r="2.5" fill="var(--gold)"/></svg></span><span>48 Larchmere Road,<br>Unit 7, Westhaven 4021</span></div>
  <div class="contact-item"><span class="contact-ring"><svg width="22" height="22" viewBox="0 0 22 22"><path d="M4 3h5l2 5-3 2a10 10 0 0 0 4 4l2-3 5 2v5a2 2 0 0 1-2 2A17 17 0 0 1 2 5a2 2 0 0 1 2-2z" fill="none" stroke="#fff" stroke-width="1.6"/></svg></span>180 555 0147</div>
</div>
<h3 class="abs form-heading" style="left:485px;top:2686px">Fill out the form below, and we'll contact you shortly.</h3>
<div class="abs form-field" style="left:485px;top:2738px;width:290px">Your Name</div>
<div class="abs form-field" style="left:811px;top:2738px;width:290px">Company</div>
<div class="abs form-field" style="left:485px;top:2792px;width:290px">Your Email</div>
<div class="abs form-field" style="left:811px;top:2792px;width:290px">Phone</div>
<div class="abs form-field" style="left:485px;top:2846px;width:616px;height:87px">How can we help you?</div>
<div class="abs btn-gold form-send">Send Now</div>
<div class="abs footer-rule"></div>
<p class="abs copyright">Copyright © 2017 zumra. All rights reserved</p>
<span class="abs social" style="left:978px"></span>
<span class="abs social" style="left:1020px"></span>
<span class="abs social" style="left:1062px"></span>

</body>
</html>
```